Simplified Double Diamond Diagram for Book

I need a simplified version of the Double Diamond Diagram for a book I am working on. I would like to represent the diagram with the following image/text:
- Two diamonds connected (as in each of the sample photos)
- Inclusion of "Diverge" "Converge" above each of the sides of the diamonds as shown in sample image 1 - without elaborative text
- Inclusion of "Problem" and "Solution" in each diamond as is shown in the example image 2
- I need a color version and black/white version of the image that can be turned into a mono-color version in the book.

```html
<!DOCTYPE html>
<html lang="en">
<head>
<meta charset="utf-8">
<title>Double Diamond Diagram</title>
<link rel="stylesheet" href="https://fonts.googleapis.com/css2?family=Inter:wght@800;900&display=swap">
<style>
  :root {
    --ink: #000000;
    --paper: #ffffff;
    --problem-stroke: #1a86b0;
    --problem-diverge: #66bfd6;
    --problem-converge: #95d3ea;
    --solution-stroke: #d47a12;
    --solution-diverge: #efa46a;
    --solution-converge: #f9c798;
    --label-size: 27px;
    --title-size: 25px;
  }
  html, body {
    margin: 0;
    padding: 0;
    width: 1200px;
    height: 1200px;
    overflow: hidden;
    background: var(--paper);
  }
  .diagram {
    display: block;
    width: 1200px;
    height: 1200px;
  }
  .phase-label,
  .diamond-title {
    font-family: "Inter", "Helvetica Neue", Arial, sans-serif;
    font-weight: 900;
    text-anchor: middle;
    dominant-baseline: central;
  }
  .phase-label { font-size: var(--label-size); letter-spacing: -0.5px; }
  .diamond-title { font-size: var(--title-size); letter-spacing: -0.5px; }

  .diamond-outline { fill: none; stroke-width: 8; stroke-linejoin: miter; }
  .axis { fill: none; stroke-width: 1; stroke-dasharray: 5 4; }

  /* mono version */
  .mono .diamond-outline { stroke: var(--ink); }
  .mono .half { fill: var(--paper); }
  .mono .axis { stroke: var(--ink); }
  .mono .phase-label,
  .mono .diamond-title { fill: var(--ink); }

  /* colour version */
  .colour .diamond-title { fill: var(--paper); }
  .colour .problem .diamond-outline { stroke: var(--problem-stroke); }
  .colour .problem .phase-label { fill: var(--problem-stroke); }
  .colour .problem .half-diverge { fill: var(--problem-diverge); }
  .colour .problem .half-converge { fill: var(--problem-converge); }
  .colour .problem .axis { stroke: var(--problem-stroke); opacity: 0.35; }
  .colour .solution .diamond-outline { stroke: var(--solution-stroke); }
  .colour .solution .phase-label { fill: var(--solution-stroke); }
  .colour .solution .half-diverge { fill: var(--solution-diverge); }
  .colour .solution .half-converge { fill: var(--solution-converge); }
  .colour .solution .axis { stroke: var(--solution-stroke); opacity: 0.35; }
</style>
</head>
<body>
<svg class="diagram" viewBox="0 0 875 875" xmlns="http://www.w3.org/2000/svg" role="img" aria-label="Double Diamond diagram in mono and colour versions">

  <g class="version mono">
    <g class="diamond problem" transform="translate(252,229)">
      <polygon class="half half-diverge" points="-184,0 0,-184 0,184"/>
      <polygon class="half half-converge" points="0,-184 184,0 0,184"/>
      <line class="axis" x1="0" y1="-184" x2="0" y2="184"/>
      <polygon class="diamond-outline" points="-184,0 0,-184 184,0 0,184"/>
      <text class="phase-label" transform="translate(-116,-110) rotate(-45)">DIVERGE</text>
      <text class="phase-label" transform="translate(111,-113) rotate(45)">CONVERGE</text>
      <text class="diamond-title" x="0" y="0">PROBLEM</text>
    </g>
    <g class="diamond solution" transform="translate(621,229)">
      <polygon class="half half-diverge" points="-184,0 0,-184 0,184"/>
      <polygon class="half half-converge" points="0,-184 184,0 0,184"/>
      <line class="axis" x1="0" y1="-184" x2="0" y2="184"/>
      <polygon class="diamond-outline" points="-184,0 0,-184 184,0 0,184"/>
      <text class="phase-label" transform="translate(-116,-110) rotate(-45)">DIVERGE</text>
      <text class="phase-label" transform="translate(111,-113) rotate(45)">CONVERGE</text>
      <text class="diamond-title" x="0" y="0">SOLUTION</text>
    </g>
  </g>

  <g class="version colour">
    <g class="diamond problem" transform="translate(252,647)">
      <polygon class="half half-diverge" points="-184,0 0,-184 0,184"/>
      <polygon class="half half-converge" points="0,-184 184,0 0,184"/>
      <line class="axis" x1="0" y1="-184" x2="0" y2="184"/>
      <polygon class="diamond-outline" points="-184,0 0,-184 184,0 0,184"/>
      <text class="phase-label" transform="translate(-116,-110) rotate(-45)">DIVERGE</text>
      <text class="phase-label" transform="translate(111,-113) rotate(45)">CONVERGE</text>
      <text class="diamond-title" x="0" y="0">PROBLEM</text>
    </g>
    <g class="diamond solution" transform="translate(621,647)">
      <polygon class="half half-diverge" points="-184,0 0,-184 0,184"/>
      <polygon class="half half-converge" points="0,-184 184,0 0,184"/>
      <line class="axis" x1="0" y1="-184" x2="0" y2="184"/>
      <polygon class="diamond-outline" points="-184,0 0,-184 184,0 0,184"/>
      <text class="phase-label" transform="translate(-116,-110) rotate(-45)">DIVERGE</text>
      <text class="phase-label" transform="translate(111,-113) rotate(45)">CONVERGE</text>
      <text class="diamond-title" x="0" y="0">SOLUTION</text>
    </g>
  </g>
</svg>
</body>
</html>
```